Brochure Design Project

Need a new look. Customer wants to update 10 year old literature. Very similar "text content" and color scheme only. Need a new modern look. Clean fonts...maybe distressed fonts. Nice salon. Would like brochure to be consistent with their decor...possibly "curvey" graphics maybe simple die-cut if cost effective to produce. Use your imagination! Showed them some pixel harbor work that they liked the look of and I will share these details so you have a feel for the type of work we are looking for.
Updates

Reason: My customer has reviewed the art submissions and though she likes the ideas presented, she has indicated that she needs to stay more consistent with some other collateral which means she would prefer a more mono-chromatic (maybe two or three colors but not a full color glossy brochure. Keeping in mind that she would like a matte look please offer design selections. She has sent me some images of the other collateral she would possibly like to coordinate with which I can send via email upon request.

Target Market(s)

Salon Patrons

Industry/Entity Type

Salon

Requirements
Must have
• Packaged InDesign file upon completion so we can edit down the line(update prices etc.) High Res PDF with marks and bleeds. Must fit into No. 10 envelope(4.125" x 9.5") once folded...I am thinking 9x16 but am open to ideas.
Should not have
• photos...or limit

```html
<!DOCTYPE html>
<html lang="en">
<head>
<meta charset="utf-8">
<title>Lumen Salon Spa – Brochure Cover</title>
<link rel="stylesheet" href="https://fonts.googleapis.com/css2?family=Ubuntu:ital,wght@0,400;0,700;1,400;1,700&display=swap">
<style>
  :root {
    --backdrop: #2a2a2b;
    --lime: #c9d82b;
    --lime-light: #e2ec52;
    --lime-deep: #a9ba1c;
    --lime-shadow: #b5c522;
    --ink: #33382a;
    --logo-ink: #2e3130;
    --rule: #ffffff;
  }
  * { box-sizing: border-box; margin: 0; padding: 0; }
  html, body {
    width: 1028px; height: 1200px; overflow: hidden;
    background: var(--backdrop);
  }
  .canvas {
    position: relative; width: 1028px; height: 1200px;
  }
  .brochure-panel {
    position: absolute; left: 274px; top: 45px;
    width: 480px; height: 1110px;
    background: radial-gradient(ellipse at 50% 45%, var(--lime-light) 0%, var(--lime) 70%, var(--lime-shadow) 100%);
    overflow: hidden;
  }
  .panel-waves {
    position: absolute; inset: 0; width: 100%; height: 100%;
  }
  .brand {
    position: absolute; left: 0; right: 0; top: 440px;
    display: flex; align-items: center; justify-content: center; gap: 14px;
  }
  .brand-dot {
    width: 18px; height: 18px; border-radius: 50%;
    background: var(--logo-ink);
  }
  .brand-name {
    font-family: "Ubuntu", sans-serif; font-weight: 700;
    font-size: 42px; color: var(--logo-ink); letter-spacing: 0.5px;
  }
  .divider {
    position: absolute; left: 56px; right: 56px; top: 520px;
    height: 3px; background: var(--rule);
  }
  .intro {
    position: absolute; left: 56px; right: 56px; top: 552px;
    font-family: "Ubuntu", sans-serif; font-size: 16.5px; line-height: 23px;
    color: var(--ink); text-align: justify; letter-spacing: 0.4px;
  }
  .intro em { font-weight: 700; font-style: italic; }
  .contact {
    position: absolute; right: 0; left: 0; bottom: 34px;
    text-align: center;
    font-family: "Ubuntu", sans-serif; font-size: 12.5px; line-height: 17px;
    color: var(--ink); letter-spacing: 0.8px;
  }
  .contact i { font-style: italic; }
  .contact b { font-weight: 700; }
</style>
</head>
<body>
<main class="canvas">
  <section class="brochure-panel">
    <svg class="panel-waves" viewBox="0 0 480 1110" preserveAspectRatio="none" aria-hidden="true">
      <path d="M0 110 C120 60 300 70 480 140 L480 0 L0 0 Z" fill="var(--lime)" opacity="0.7"/>
      <path d="M0 250 C110 180 260 130 480 150 L480 215 C300 190 160 230 0 300 Z" fill="var(--lime-deep)" opacity="0.35"/>
      <path d="M0 300 C140 230 300 210 480 240 L480 280 C310 260 150 290 0 350 Z" fill="var(--lime-light)" opacity="0.45"/>
      <path d="M0 860 C130 940 300 900 480 820 L480 1110 L0 1110 Z" fill="var(--lime-deep)" opacity="0.25"/>
      <path d="M0 930 C150 1000 320 960 480 900 L480 1110 L0 1110 Z" fill="var(--lime)" opacity="0.6"/>
    </svg>

    <div class="brand">
      <span class="brand-dot"></span>
      <span class="brand-name">Lumen Salon Spa</span>
    </div>

    <div class="divider"></div>

    <p class="intro">At <em>lumen salon and spa</em> we are dedicated to making every visit a positive experience. Whether you are here for a day of pampering or for your regular salon appointment, our staff of experienced professionals are dedicated to meeting your every need. Escape the stresses of life and discover a new environment of relaxation and beauty.</p>

    <address class="contact">
      555 | <i>lumenspa (586 3772)</i><br>
      www.<b>lumensalonspa</b>.com<br>
      hello@lumensalonspa.com
    </address>
  </section>
</main>
</body>
</html>
```